Website for Plumbing Company, Sir FlowBoiler

I need a 7-page fully HTML-coded website for my plumbing company, Sir FlowBoiler. We specialize in installation, repair, and replacement of both gas and electric water heaters. Although we offer both tankless (on-demand) water heaters and standard (with tank) water heaters, most of our business is related to standard (with tank) water heaters in the USA market.

These are the pages I need:
1. Home page with sections such as About Us, Our Services, Why Choose Us, Testimonials, Location Map (Palm Beach County Florida), Quote Request Form, Join Our Newsletter, Mission Statement, etc.

2. Gas Water Heaters

3. Electric Water Heaters

4. Tankless Water Heaters

5. About Us

6. Contact Us

7. Privacy Policy, Terms & Conditions

Be sure to mention the following points:
1. Same-Day Service
2. Best Price Guarantee
3. 100% Satisfaction Rating
4. 15-Year Warranty on Water Heater & Parts
5. Lifetime Warranty on Workmanship
*All Warranties are Transferrable Upon Home Sale

Once design is selected and finalized, I need the website coded in a standard HTML/CSS and temporarily hosted on your development server so I can see the website functionality that is not observable from screenshots, such as section animations, etc. Once those details are finalized, I will move the source code to my server and complete the project.

Target Market(s)

Residential Home Owners and Business Owners

Industry/Entity Type

Plumbing, Home Services, Remodeling, Construction

Coding

Coded - Design and coding required

Number of Pages Required

5+ page

Colors
0054AA
0677BA
7BADD7
CADEEF
E8F1F8
FFC000
F8CF3A
FAE287
FDF2CF
FEFAEE
EE7325
F08F49
F5BC92
FAE3D3
FDF4ED

Requirements
Must have
• Clean, colorful, and professional

```html
<!DOCTYPE html>
<html lang="en">
<head>
<meta charset="utf-8">
<title>Sir FlowBoiler – Water Heater Services</title>
<link href="https://fonts.googleapis.com/css2?family=Poppins:wght@400;500;600;700;800&display=swap" rel="stylesheet">
<style>
:root{
  --navy:#0b2e6f;
  --navy-deep:#0a2458;
  --navy-foot:#0c2a63;
  --blue:#0054AA;
  --blue-2:#0677BA;
  --blue-3:#7BADD7;
  --blue-4:#CADEEF;
  --blue-5:#E8F1F8;
  --orange:#EE7325;
  --orange-red:#f0461c;
  --yellow:#FFC000;
  --ink:#14213d;
  --text:#3a4356;
  --grey-bg:#eff2f6;
  --white:#ffffff;
}
*{box-sizing:border-box;margin:0;padding:0}
html,body{width:1200px;height:4141px;overflow:hidden}
body{font-family:"Poppins",sans-serif;color:var(--text);background:var(--white);position:relative}
.abs{position:absolute}
.btn{position:absolute;display:flex;align-items:center;justify-content:center;border-radius:30px;font-weight:700;font-size:10.5px;text-transform:uppercase;letter-spacing:.2px}
.btn-orange{background:linear-gradient(90deg,var(--orange-red),var(--orange) 45%,var(--yellow));color:#fff}
.btn-outline{border:2px solid var(--navy);color:var(--navy);background:#fff}
.btn-outline-light{border:1.5px solid #fff;color:#fff}

/* hero */
.hero{position:absolute;left:0;top:0;width:1200px;height:710px;background:radial-gradient(ellipse at 70% 40%,#14479e 0%,#0d3883 45%,#0a2c6e 100%)}
.hero-wave{position:absolute;left:0;top:600px}
.topbar{position:absolute;left:337px;top:0;width:525px;height:40px;background:linear-gradient(90deg,#1b62c6,#2c7ee0);border-radius:0 0 30px 30px;display:flex;align-items:center;padding-left:26px;gap:24px;font-size:9.5px;color:#fff;font-weight:500}
.topbar .item{display:flex;align-items:center;gap:6px}
.topbar .social{margin-left:auto;margin-right:22px;display:flex;gap:6px}
.topbar .social span{width:16px;height:16px;border-radius:50%;background:rgba(255,255,255,.25)}
.brand{position:absolute;display:flex;align-items:center;gap:10px;font-weight:800;color:#fff}
.brand .mark{border-radius:50%;background:var(--blue-2)}
.nav{position:absolute;left:478px;top:76px;display:flex;gap:31px;font-size:9.5px;font-weight:600;color:#fff;text-transform:uppercase;align-items:center}
.nav .home{width:11px;height:11px}
.hero h1{position:absolute;left:117px;top:244px;font-size:34px;line-height:41px;font-weight:700;color:#fff;letter-spacing:-.3px}
.hero h1 em{font-style:normal;color:#ff7a1a}
.hero .lead{position:absolute;left:117px;top:330px;width:410px;font-size:10px;line-height:15px;color:#e6edf8}
.hero ul{position:absolute;left:117px;top:368px;list-style:none;font-size:10px;color:#fff;line-height:20px}
.hero li{display:flex;align-items:center;gap:8px}
.hero li i{width:10px;height:10px;border-radius:50%;background:var(--blue-3);display:inline-block}
.dots{position:absolute;left:117px;top:608px;display:flex;gap:6px}
.dots span{width:8px;height:8px;border-radius:50%;background:rgba(255,255,255,.45)}
.dots span.on{background:var(--orange)}
.hero-art{position:absolute;left:607px;top:177px;width:460px;height:578px;border-radius:40px;background:linear-gradient(160deg,#f1f3f6 0%,#cfd6df 55%,#3b5fb0 100%)}

/* why */
.section-title{position:absolute;width:1200px;text-align:center;font-weight:700;color:var(--ink);font-size:32px;line-height:40px;letter-spacing:-.5px}
.why-item{position:absolute;top:949px;width:150px;text-align:center}
.why-item .ring{width:104px;height:104px;margin:0 auto;border-radius:50%;border:1.5px solid var(--blue-2);display:flex;align-items:center;justify-content:center;background:#fff}
.why-item p{margin-top:20px;font-size:10.5px;line-height:13.5px;font-weight:600;color:var(--ink)}

/* about */
.about-ring{position:absolute;left:-15px;top:1260px;width:554px;height:554px;border-radius:50%;border:7px solid var(--blue);clip-path:inset(0 0 0 0)}
.about-photo{position:absolute;left:-6px;top:1269px;width:536px;height:536px;border-radius:50%;background:linear-gradient(135deg,#5c7a44 0%,#9db27d 30%,#d9dfe6 50%,#b8452d 75%,#2a4aa0 100%)}
.play{position:absolute;left:357px;top:1701px;width:94px;height:94px;border-radius:50%;background:var(--navy-deep);display:flex;align-items:center;justify-content:center}
.about h2{position:absolute;left:591px;top:1337px;font-size:30px;font-weight:700;color:var(--ink);letter-spacing:-.4px}
.about p{position:absolute;left:591px;width:490px;font-size:10.3px;line-height:19px;color:var(--text)}
.about b{color:var(--ink);font-weight:600}

/* services */
.grey{position:absolute;left:0;top:1895px;width:1200px;height:590px;background:var(--grey-bg)}
.grey-curve{position:absolute;left:0;top:1665px}
.mascot{position:absolute;left:859px;top:1790px;width:250px;height:266px;border-radius:40px 40px 0 0;background:linear-gradient(160deg,#dfe5ee,#c23b2d 55%,#1c4fb0)}
.card{position:absolute;top:2056px;width:236px;height:313px;border-radius:6px;overflow:hidden}
.card .photo{position:absolute;inset:0;background:linear-gradient(160deg,#c9ced5 0%,#8a929c 45%,#3d4a60 100%)}
.card .shade{position:absolute;inset:0;background:linear-gradient(180deg,rgba(10,70,190,0) 40%,rgba(15,80,200,.85) 75%,#1553c7 100%)}
.card .badge{position:absolute;left:32px;top:30px;width:50px;height:50px;border-radius:50%;background:#f04a1e;display:flex;align-items:center;justify-content:center}
.card h3{position:absolute;left:39px;top:247px;font-size:17px;line-height:20px;font-weight:700;color:#fff}

/* reviews */
.reviews h2{position:absolute;left:166px;top:2735px;font-size:32px;font-weight:700;color:var(--ink);letter-spacing:-.5px}
.reviews .quote{position:absolute;left:166px;top:2790px;width:400px;font-size:14.5px;line-height:21px;color:var(--ink)}
.reviews .stars{position:absolute;left:166px;top:2862px;display:flex;gap:3px}
.reviews .name{position:absolute;left:166px;top:2898px;font-size:14.5px;font-weight:600;color:var(--ink)}
.reviews .place{position:absolute;left:166px;top:2921px;font-size:14px;color:var(--text)}
.arrow{position:absolute;top:2888px;width:46px;height:46px;border-radius:50%;display:flex;align-items:center;justify-content:center}

/* quote form */
.quote-form{position:absolute;left:676px;top:2581px;width:371px;height:446px;border-radius:48px;background:linear-gradient(180deg,#f2431c 0%,#f46b1a 55%,#fdae16 100%)}
.quote-form h2{position:absolute;top:34px;width:100%;text-align:center;color:#fff;font-size:31px;font-weight:700;letter-spacing:-.4px}
.field{position:absolute;height:38px;border-radius:20px;background:#fff;font-size:11.5px;font-weight:600;color:var(--ink);padding-left:18px;display:flex;align-items:center}
.submit{position:absolute;left:98px;top:371px;width:174px;height:40px;border-radius:20px;background:var(--navy-deep);color:#fff;font-size:9.5px;font-weight:700;display:flex;align-items:center;justify-content:center}

/* area */
.map{position:absolute;left:152px;top:3051px;width:458px;height:458px;background:linear-gradient(160deg,#f2f4fb 0%,#e3e8f6 60%,#dbe1f2 100%);border-radius:12px}
.area h2{position:absolute;left:671px;top:3190px;font-size:31px;line-height:40px;font-weight:700;color:var(--ink);letter-spacing:-.4px}
.area p{position:absolute;left:675px;top:3280px;width:360px;font-size:10.3px;line-height:18.5px;color:var(--text)}

/* footer */
.footer{position:absolute;left:0;top:3590px;width:1200px;height:551px;background:var(--navy-foot)}
.foot-curve{position:absolute;left:0;top:3555px}
.van{position:absolute;left:482px;top:3533px;width:241px;height:121px;border-radius:30px;background:linear-gradient(160deg,#ffffff,#dde3ec 60%,#3366c4)}
.news-title{position:absolute;top:3700px;width:1200px;text-align:center;font-size:31px;font-weight:700;color:#fff}
.news-input{position:absolute;left:334px;top:3758px;width:530px;height:40px;border-radius:22px;background:#fff;display:flex;align-items:center;padding-left:18px;gap:8px;font-size:10px;color:#6b7385}
.news-btn{position:absolute;left:754px;top:3758px;width:110px;height:40px;border-radius:22px;background:linear-gradient(90deg,var(--orange-red),var(--yellow));color:#fff;font-size:10.5px;font-weight:700;display:flex;align-items:center;justify-content:center}
.foot-col{position:absolute;top:3880px;color:#fff}
.foot-col h4{font-size:16px;font-weight:600;margin-bottom:12px}
.foot-col li{list-style:none;font-size:10px;line-height:19px;color:#dbe4f3}
.pay{display:flex;flex-wrap:wrap;gap:6px;width:130px}
.pay span{width:36px;height:24px;border-radius:4px;background:#fff}
.foot-line{position:absolute;left:0;top:4076px;width:1200px;height:65px;background:#0a2455}
.copy{position:absolute;left:164px;top:4098px;font-size:10px;color:#fff}
.foot-social{position:absolute;left:945px;top:4090px;display:flex;gap:10px}
.foot-social span{width:24px;height:24px;border-radius:50%;background:rgba(255,255,255,.15)}
.chat{position:absolute;left:1110px;top:4063px;width:46px;height:46px;border-radius:50%;background:linear-gradient(135deg,#f04a1e,#ff9a1a);display:flex;align-items:center;justify-content:center}
</style>
</head>
<body>

<!-- HERO -->
<header class="hero">
  <div class="topbar">
    <div class="item"><svg width="10" height="10" viewBox="0 0 24 24"><path fill="#ff7a1a" d="M6.6 10.8a15 15 0 0 0 6.6 6.6l2.2-2.2c.3-.3.7-.4 1-.2 1.1.4 2.3.6 3.6.6.6 0 1 .4 1 1V20c0 .6-.4 1-1 1A17 17 0 0 1 3 4c0-.6.4-1 1-1h3.5c.6 0 1 .4 1 1 0 1.3.2 2.5.6 3.6.1.3 0 .7-.2 1z"/></svg>Phone: 123-456-7890</div>
    <div class="item"><svg width="11" height="9" viewBox="0 0 24 18"><rect x="1" y="1" width="22" height="16" rx="2" fill="#ff7a1a"/><path d="M2 2l10 8 10-8" stroke="#fff" stroke-width="2" fill="none"/></svg>Email: info@sirflowboiler.com</div>
    <div class="social"><span></span><span></span><span></span><span></span></div>
  </div>

  <div class="brand" style="left:128px;top:40px;font-size:24px"><span class="mark" style="width:34px;height:34px"></span>Sir FlowBoiler</div>

  <nav class="nav">
    <svg class="home" viewBox="0 0 24 24"><path fill="#ff7a1a" d="M12 3l10 9h-3v9h-5v-6h-4v6H5v-9H2z"/></svg>
    <span>Services ⌄</span><span>About Us</span><span>Reviews</span><span>Contact Us</span><span>Get a Free Quote</span>
  </nav>
  <div class="btn btn-orange" style="left:938px;top:67px;width:109px;height:33px">Book Online</div>

  <h1>Fast, Reliable Water <em>Heater</em><br>Services You Can Trust</h1>
  <p class="lead">Expert installation, repair, and replacement of gas and electric water heaters across Palm Beach County, Florida.</p>
  <ul>
    <li><i></i>Same-Day Service Available</li>
    <li><i></i>Best Price Guarantee</li>
    <li><i></i>100% Satisfaction Rating</li>
  </ul>
  <div class="btn btn-orange" style="left:119px;top:447px;width:150px;height:41px">Get a Free Quote</div>
  <div class="btn btn-outline-light" style="left:275px;top:447px;width:226px;height:41px">Call Now for Same-Day Service</div>
  <div class="dots"><span></span><span></span><span class="on"></span><span></span></div>
</header>
<svg class="hero-wave" width="1200" height="120" viewBox="0 0 1200 120" preserveAspectRatio="none"><path d="M0 68 C 220 120, 420 120, 640 90 C 860 60, 1040 40, 1200 55 L1200 120 L0 120 Z" fill="#fff"/></svg>
<div class="hero-art" role="img" aria-label="Illustrated plumber mascot carrying a water heater beside a large white tank water heater"></div>

<!-- WHY -->
<h2 class="section-title" style="top:835px">Why Homeowners Choose<br>Sir FlowBoiler</h2>
<div class="why-item" style="left:115px"><div class="ring"><svg width="50" height="50" viewBox="0 0 50 50" fill="none" stroke="#243a6b" stroke-width="2"><circle cx="30" cy="28" r="13"/><path d="M30 20v8l6 4" stroke="#ee7325"/><rect x="6" y="24" width="14" height="10" rx="2"/></svg></div><p>Same-Day Service No waiting days for hot water</p></div>
<div class="why-item" style="left:282px"><div class="ring"><svg width="50" height="50" viewBox="0 0 50 50" fill="none" stroke="#243a6b" stroke-width="2"><circle cx="25" cy="17" r="9" stroke="#ee7325"/><path d="M25 12v10M22 15h5a2 2 0 0 1 0 4h-4a2 2 0 0 0 0 4h5" stroke="#ee7325" stroke-width="1.5"/><path d="M8 30l8 12h6M42 30l-8 12h-6"/></svg></div><p>Best Price Guarantee Fair, upfront pricing</p></div>
<div class="why-item" style="left:444px"><div class="ring"><svg width="50" height="50" viewBox="0 0 50 50" fill="none" stroke="#243a6b" stroke-width="2"><path d="M12 8l2 4 4 .5-3 3 .8 4-3.8-2-3.8 2 .8-4-3-3 4-.5zM38 8l2 4 4 .5-3 3 .8 4-3.8-2-3.8 2 .8-4-3-3 4-.5z" stroke="#ee7325" stroke-width="1.5"/><circle cx="25" cy="24" r="6"/><path d="M14 44c0-7 5-11 11-11s11 4 11 11"/></svg></div><p>100% Customer Satisfaction Rating</p></div>
<div class="why-item" style="left:612px"><div class="ring"><svg width="50" height="50" viewBox="0 0 50 50" fill="none" stroke="#243a6b" stroke-width="2"><path d="M16 18a9 9 0 0 1 18 0z" stroke="#ee7325"/><circle cx="25" cy="23" r="6"/><path d="M12 45c0-8 6-13 13-13s13 5 13 13M25 32v13"/></svg></div><p>Licensed, Experienced Technicians</p></div>
<div class="why-item" style="left:771px"><div class="ring"><svg width="50" height="50" viewBox="0 0 50 50" fill="none" stroke="#243a6b" stroke-width="2"><circle cx="27" cy="18" r="10" stroke="#ee7325"/><path d="M27 12v6l4 3" stroke="#ee7325"/><path d="M6 36l8-4h10l8 4 8-6M6 44h28"/></svg></div><p>Clean, Professional, On-Time Service</p></div>
<div class="why-item" style="left:938px"><div class="ring"><svg width="50" height="50" viewBox="0 0 50 50" fill="none" stroke="#243a6b" stroke-width="2"><rect x="14" y="8" width="22" height="34" rx="3"/><rect x="19" y="14" width="12" height="8" rx="1" stroke="#ee7325"/><circle cx="25" cy="31" r="3" stroke="#ee7325"/></svg></div><p>Focused Water Heater Specialists (Not General Plumbers)</p></div>
<div class="btn btn-orange" style="left:435px;top:1143px;width:148px;height:42px">Get a Free Quote</div>
<div class="btn btn-outline" style="left:591px;top:1143px;width:175px;height:42px">Speak to Our Expert</div>

<!-- ABOUT -->
<section class="about">
  <div class="about-ring"></div>
  <div class="about-photo" role="img" aria-label="Smiling plumber with arms crossed in front of a branded service van"></div>
  <div class="play"><svg width="26" height="28" viewBox="0 0 26 28"><path d="M4 2l20 12L4 26z" fill="#fff"/></svg></div>
  <h2>About Sir FlowBoiler</h2>
  <p style="top:1392px">Sir FlowBoiler is a trusted plumbing company specializing exclusively in <b>water heater services</b>. We proudly serve homeowners across Palm Beach County, Florida, providing professional installation, repair, and replacement of <b>gas and electric water heaters</b>.</p>
  <p style="top:1454px">While we offer both <b>tankless (on-demand)</b> and <b>standard tank water heaters</b>, our expertise is strongly rooted in <b>traditional tank water heater systems</b>, which remain the most reliable and cost-effective solution for many American homes.</p>
  <div class="btn btn-orange" style="left:583px;top:1530px;width:150px;height:41px">Get a Free Quote</div>
  <div class="btn btn-outline" style="left:740px;top:1530px;width:175px;height:41px">Speak to Our Expert</div>
</section>

<!-- SERVICES -->
<svg class="grey-curve" width="1200" height="240" viewBox="0 0 1200 240" preserveAspectRatio="none"><path d="M0 232 C 260 240, 520 190, 760 90 C 900 35, 1060 10, 1200 12 L1200 240 L0 240 Z" fill="#eff2f6"/></svg>
<div class="grey"></div>
<div class="mascot" role="img" aria-label="Plumber mascot lifting a water heater over his shoulder"></div>
<h2 class="section-title" style="top:1982px">Our Water Heater Services</h2>
<div class="card" style="left:119px"><div class="photo" role="img" aria-label="Technician installing a wall-mounted water heater"></div><div class="shade"></div><div class="badge"><svg width="22" height="26" viewBox="0 0 22 26" fill="none" stroke="#fff" stroke-width="2"><rect x="3" y="2" width="16" height="22" rx="2"/><circle cx="11" cy="15" r="3"/></svg></div><h3>Water Heater<br>Installation</h3></div>
<div class="card" style="left:361px"><div class="photo" role="img" aria-label="Technician repairing a water heater control"></div><div class="shade"></div><div class="badge"><svg width="22" height="26" viewBox="0 0 22 26" fill="none" stroke="#fff" stroke-width="2"><rect x="3" y="2" width="16" height="22" rx="2"/><circle cx="11" cy="15" r="3"/></svg></div><h3>Water Heater<br>Repair</h3></div>
<div class="card" style="left:603px"><div class="photo" role="img" aria-label="Plumber replacing a water heater connection"></div><div class="shade"></div><div class="badge"><svg width="22" height="26" viewBox="0 0 22 26" fill="none" stroke="#fff" stroke-width="2"><rect x="3" y="2" width="16" height="22" rx="2"/><circle cx="11" cy="15" r="3"/></svg></div><h3>Water Heater<br>Replacement</h3></div>
<div class="card" style="left:845px"><div class="photo" role="img" aria-label="Technician servicing a tankless water heater"></div><div class="shade"></div><div class="badge"><svg width="22" height="26" viewBox="0 0 22 26" fill="none" stroke="#fff" stroke-width="2"><rect x="3" y="2" width="16" height="22" rx="2"/><circle cx="11" cy="15" r="3"/></svg></div><h3>Tankless Water<br>Heaters</h3></div>

<!-- REVIEWS -->
<section class="reviews">
  <svg class="abs" style="left:164px;top:2634px" width="110" height="72" viewBox="0 0 110 72"><defs><linearGradient id="qg" x1="0" x2="1"><stop offset="0" stop-color="#7BADD7"/><stop offset="1" stop-color="#0054AA"/></linearGradient></defs><path d="M26 72a26 26 0 1 1 24-36C50 14 38 4 28 0c20 2 30 20 30 38a26 26 0 0 1-32 34zM78 72a26 26 0 1 1 24-36C102 14 90 4 80 0c20 2 30 20 30 38a26 26 0 0 1-32 34z" fill="url(#qg)"/></svg>
  <h2>Client Reviews</h2>
  <p class="quote">"Best price guarantee really works! Same-day service, polite technicians, and thorough explanation of warranties. Very satisfied with their work."</p>
  <div class="stars">
    <svg width="120" height="22" viewBox="0 0 120 22"><g fill="#f6a81c"><path id="st" d="M11 1l3 6.6 7 .8-5.3 4.8 1.5 7L11 16.7 4.8 20.2l1.5-7L1 8.4l7-.8z"/><use href="#st" x="24"/><use href="#st" x="48"/><use href="#st" x="72"/><use href="#st" x="96"/></g></svg>
  </div>
  <div class="name">Daniel K.,</div>
  <div class="place">Boynton Beach, FL</div>
  <div class="arrow" style="left:491px;background:#e3e7ee"><svg width="16" height="12" viewBox="0 0 16 12"><path d="M15 6H2M6 1L1 6l5 5" stroke="#243a6b" stroke-width="1.5" fill="none"/></svg></div>
  <div class="arrow" style="left:545px;background:var(--navy-deep)"><svg width="16" height="12" viewBox="0 0 16 12"><path d="M1 6h13M10 1l5 5-5 5" stroke="#fff" stroke-width="1.5" fill="none"/></svg></div>
</section>

<!-- QUOTE FORM -->
<form class="quote-form">
  <h2>Request a Quote</h2>
  <div class="field" style="left:34px;top:105px;width:148px">Name</div>
  <div class="field" style="left:190px;top:105px;width:148px">Phone</div>
  <div class="field" style="left:34px;top:154px;width:148px">Email</div>
  <div class="field" style="left:190px;top:154px;width:148px">Address</div>
  <div class="field" style="left:34px;top:203px;width:304px;justify-content:space-between;padding-right:18px">Type of Service Needed<span style="font-size:9px">▼</span></div>
  <div class="field" style="left:34px;top:254px;width:304px;height:98px;align-items:flex-start;padding-top:12px;border-radius:16px">Message</div>
  <div class="submit">Get My Free Quote</div>
</form>

<!-- SERVICE AREA -->
<section class="area">
  <div class="map" role="img" aria-label="Outline map of Florida counties with Palm Beach County highlighted in orange"></div>
  <h2>Proudly Serving Palm<br>Beach County, Florida</h2>
  <p>We provide water heater services throughout Palm Beach County, including West Palm Beach, Boca Raton, Delray Beach, Boynton Beach, and surrounding areas.</p>
  <div class="btn btn-orange" style="left:667px;top:3357px;width:150px;height:40px">View Cover Areas</div>
</section>

<!-- FOOTER -->
<svg class="foot-curve" width="1200" height="40" viewBox="0 0 1200 40" preserveAspectRatio="none"><path d="M0 38 C 300 10, 700 0, 1200 18 L1200 40 L0 40 Z" fill="#0c2a63"/></svg>
<footer class="footer"></footer>
<div class="van" role="img" aria-label="White branded service van"></div>
<h2 class="news-title">Subscribe Newsletter</h2>
<div class="news-input"><svg width="11" height="9" viewBox="0 0 24 18"><rect x="1" y="1" width="22" height="16" rx="2" fill="none" stroke="#6b7385" stroke-width="2"/><path d="M2 2l10 8 10-8" stroke="#6b7385" stroke-width="2" fill="none"/></svg>Enter your email address...</div>
<div class="news-btn">Subscribe</div>

<div class="brand" style="left:190px;top:3925px;font-size:30px"><span class="mark" style="width:40px;height:40px"></span>Sir FlowBoiler</div>

<div class="foot-col" style="left:543px"><h4>Quick Links</h4><ul><li>Home</li><li>About Us</li><li>Services</li><li>Contact Us</li><li>Get a Free Quote</li></ul></div>
<div class="foot-col" style="left:699px"><h4>Our Services</h4><ul><li>Gas Water Heaters</li><li>Electric Water Heaters</li><li>Tankless Water Heaters</li><li>Water Heater Repair</li><li>Water Heater Replacement</li></ul></div>
<div class="foot-col" style="left:890px"><h4>Payment</h4><div class="pay"><span></span><span></span><span></span><span></span><span></span></div></div>

<div class="foot-line"></div>
<div class="copy">© Copyright 2026, Water Heater All Rights Reserved</div>
<div class="foot-social"><span></span><span></span><span></span></div>
<div class="chat"><svg width="22" height="20" viewBox="0 0 22 20"><path d="M11 1C5.5 1 1 4.6 1 9c0 2.4 1.3 4.5 3.4 6L3 19l4.6-2.3c1.1.3 2.2.4 3.4.4 5.5 0 10-3.6 10-8S16.5 1 11 1z" fill="#fff"/><circle cx="7" cy="9" r="1.3" fill="#f04a1e"/><circle cx="11" cy="9" r="1.3" fill="#f04a1e"/><circle cx="15" cy="9" r="1.3" fill="#f04a1e"/></svg></div>

</body>
</html>
```